Business Card & Logo

Business Card Design Project & Logo

Need logo for business card

Company name is KORU electric bikes USA

Target Market(s)

Consumer

Industry/Entity Type

Sporting Good

Contact Information for Business Card

Electric Bike Business Cards, Flyers, and LOGO.

Font styles to use
Sans Serif

Colors
ffc214
ffcf3e
faa54b
fee18a
f37122

Requirements
Must have
• New look &LOGO

```html
<!DOCTYPE html>
<html lang="en">
<head>
<meta charset="utf-8">
<title>KORU electric bikes USA – Business Card</title>
<link href="https://fonts.googleapis.com/css2?family=Source+Sans+3:wght@400;600;700&display=swap" rel="stylesheet">
<style>
  :root {
    --stage: #1b1b1b;
    --paper: #f2f2f2;
    --orange: #f37122;
    --ink: #1a1a1a;
    --white: #ffffff;
  }
  * { margin: 0; padding: 0; box-sizing: border-box; }
  html, body {
    width: 1200px; height: 900px; overflow: hidden;
    background: var(--stage);
    font-family: "Source Sans 3", Arial, sans-serif;
  }
  .canvas { position: relative; width: 1200px; height: 900px; }
  .card {
    position: absolute; top: 170px;
    width: 347px; height: 561px;
    overflow: hidden;
  }
  .card--front { left: 259px; background: var(--paper); }
  .card--back { left: 631px; background: var(--orange); }

  .front__mark {
    position: absolute; left: 74px; top: 77px;
    width: 200px; height: 200px; border-radius: 50%;
    background: var(--orange);
  }
  .front__details {
    position: absolute; left: 0; right: 0; top: 345px;
    text-align: center; color: var(--ink);
  }
  .person__name {
    color: var(--orange); font-weight: 700; font-size: 22px;
    line-height: 28px; letter-spacing: 0.2px;
  }
  .person__role { font-size: 15px; line-height: 18px; }
  .contact { margin-top: 16px; font-size: 15px; line-height: 21px; }
  .contact__label { color: var(--orange); font-weight: 600; }
  .contact__web { font-weight: 700; }
  .contact__web .accent { color: var(--orange); }
  .address { margin-top: 10px; font-size: 15px; line-height: 17px; }

  .back__flash {
    position: absolute; left: 0; top: 40px; width: 347px; height: 490px;
    background: linear-gradient(135deg, rgba(255,255,255,0) 20%, rgba(255,255,255,0.09) 50%, rgba(255,255,255,0) 80%);
  }
  .back__badge {
    position: absolute; left: 20px; top: 230px;
    width: 102px; height: 102px; border-radius: 50%;
    background: var(--white);
  }
  .brand {
    position: absolute; left: 154px; top: 246px; width: 176px;
    text-align: center; color: var(--white); font-weight: 600;
  }
  .brand__name { font-size: 56px; line-height: 50px; letter-spacing: 4px; }
  .brand__tagline { font-size: 15px; line-height: 18px; letter-spacing: 2.6px; margin-top: 2px; }
  .brand__region { font-size: 10px; line-height: 12px; letter-spacing: 2px; }
</style>
</head>
<body>
<main class="canvas">
  <section class="card card--front">
    <div class="front__mark"></div>
    <div class="front__details">
      <h1 class="person__name">ALEX MORGAN</h1>
      <p class="person__role">Managing Director</p>
      <div class="contact">
        <p><span class="contact__label">P:</span> 555-014-2270</p>
        <p><span class="contact__label">E:</span> hello@koruebikes.com</p>
        <p class="contact__web"><span class="accent">www.</span>koruebikes<span class="accent">.com</span></p>
      </div>
      <p class="address">1234, Address Goes Here<br>Country Name, 123456</p>
    </div>
  </section>

  <section class="card card--back">
    <div class="back__flash" role="img" aria-label="Faint diagonal light decoration across the card"></div>
    <div class="back__badge"></div>
    <div class="brand">
      <p class="brand__name">KORU</p>
      <p class="brand__tagline">ELECTRIC BIKES</p>
      <p class="brand__region">USA</p>
    </div>
  </section>
</main>
</body>
</html>
```